CrewLedger business cards

Software for fire departments

Target Market(s)

Fire Departments

Industry/Entity Type

Business

Contact Information for Business Card

see attachments. Looking to print three sets of cards.

Requirements
Must have
• front and back
Nice to have
• rounded corners

```html
<!DOCTYPE html>
<html lang="en">
<head>
<meta charset="utf-8">
<title>CrewLedger Business Cards</title>
<link rel="stylesheet" href="https://fonts.googleapis.com/css2?family=Lato:wght@400;700;900&display=swap">
<style>
  :root {
    --bg: #2b2b2b;
    --card-white: #f7f7f7;
    --brand-red: #d8141c;
    --brand-red-dark: #a50f14;
    --ink: #1a1a1a;
    --rule: #111111;
  }
  * { box-sizing: border-box; margin: 0; padding: 0; }
  html, body {
    width: 1200px; height: 997px; overflow: hidden;
    background: var(--bg);
    font-family: "Lato", sans-serif;
  }
  .canvas { position: relative; width: 1200px; height: 997px; }

  .card {
    position: absolute;
    width: 560px; height: 320px;
    border-radius: 22px;
    overflow: hidden;
    background: var(--card-white);
    box-shadow: 0 18px 40px rgba(0,0,0,.55);
  }

  /* Front: brand side */
  .card--front { left: 80px; top: 110px; }
  .card--front .band-top {
    position: absolute; left: 0; right: 0; top: 0; height: 34px;
    background: linear-gradient(var(--brand-red), var(--brand-red-dark));
  }
  .card--front .band-bottom {
    position: absolute; left: 0; right: 0; bottom: 0; height: 70px;
    background: linear-gradient(var(--brand-red), var(--brand-red-dark));
    display: flex; align-items: center; justify-content: center;
  }
  .tagline {
    color: #f4dede; font-weight: 700; font-size: 22px; letter-spacing: .3px;
  }
  .card--front .brand-name {
    position: absolute; left: 0; right: 0; top: 34px; bottom: 70px;
    display: flex; align-items: center; justify-content: center;
    font-size: 72px;
  }
  .brand-name {
    font-weight: 900; color: var(--brand-red); letter-spacing: -1px;
  }

  /* Back: contact side */
  .card--back { left: 560px; top: 540px; }
  .card--back .rule {
    position: absolute; left: 0; right: 0; top: 222px; height: 5px;
    background: var(--rule);
  }
  .card--back .band-bottom {
    position: absolute; left: 0; right: 0; top: 227px; bottom: 0;
    background: linear-gradient(var(--brand-red), var(--brand-red-dark));
  }
  .card--back .brand-name {
    position: absolute; left: 30px; top: 80px; width: 250px;
    font-size: 46px; text-align: center; line-height: 62px;
  }
  .divider {
    position: absolute; left: 296px; top: 26px; width: 2px; height: 180px;
    background: linear-gradient(rgba(216,20,28,0), var(--brand-red) 40%, rgba(216,20,28,0));
  }
  .contact { position: absolute; left: 318px; top: 34px; }
  .person-name { font-weight: 900; font-size: 17px; color: var(--ink); letter-spacing: .5px; }
  .person-title { font-weight: 700; font-size: 13px; color: var(--brand-red); margin-top: 2px; }
  .contact-list { list-style: none; margin-top: 24px; }
  .contact-item {
    display: flex; align-items: flex-start; gap: 9px;
    font-size: 14px; color: var(--ink); margin-bottom: 10px; line-height: 18px;
  }
  .contact-icon { flex: none; width: 18px; height: 18px; }
</style>
</head>
<body>
<main class="canvas">

  <section class="card card--front" aria-label="Card front">
    <div class="band-top"></div>
    <div class="brand-name">CrewLedger</div>
    <div class="band-bottom"><p class="tagline">Smart Risk Management For Fire Services</p></div>
  </section>

  <section class="card card--back" aria-label="Card back">
    <div class="brand-name">CrewLedger</div>
    <div class="divider"></div>
    <div class="contact">
      <p class="person-name">MARK ELLISON</p>
      <p class="person-title">Chief Executive Officer</p>
      <ul class="contact-list">
        <li class="contact-item">
          <svg class="contact-icon" viewBox="0 0 18 18" aria-hidden="true">
            <circle cx="9" cy="9" r="9" fill="#d8141c"/>
            <path d="M5.5 5.5c.6-.6 1.3-.6 1.6 0l.8 1.4c.2.4.1.8-.2 1.1l-.5.4c.4.9 1.3 1.8 2.2 2.2l.4-.5c.3-.3.7-.4 1.1-.2l1.4.8c.6.3.6 1 0 1.6-.9.9-2.2 1-3.6.1-1.3-.8-2.6-2.1-3.4-3.4-.9-1.4-.7-2.7.2-3.5z" fill="#fff"/>
          </svg>
          <span>555-014-2237</span>
        </li>
        <li class="contact-item">
          <svg class="contact-icon" viewBox="0 0 18 18" aria-hidden="true">
            <circle cx="9" cy="9" r="9" fill="#d8141c"/>
            <rect x="4.5" y="5.8" width="9" height="6.4" fill="#fff"/>
            <path d="M4.5 5.8 9 9.6l4.5-3.8" fill="none" stroke="#d8141c" stroke-width="1"/>
          </svg>
          <span>mark@crewledger.com</span>
        </li>
        <li class="contact-item">
          <svg class="contact-icon" viewBox="0 0 18 18" aria-hidden="true">
            <circle cx="9" cy="9" r="9" fill="#d8141c"/>
            <path d="M9 4.2a3.2 3.2 0 0 0-3.2 3.2c0 2.4 3.2 6.2 3.2 6.2s3.2-3.8 3.2-6.2A3.2 3.2 0 0 0 9 4.2z" fill="#fff"/>
            <circle cx="9" cy="7.4" r="1.2" fill="#d8141c"/>
          </svg>
          <span>14 Harbor Mill Lane,<br>Danvers, MA 01923</span>
        </li>
      </ul>
    </div>
    <div class="rule"></div>
    <div class="band-bottom"></div>
  </section>

</main>
</body>
</html>
```